Marlow Realty Real Estate Brokerage Recruiting Flyer

We are a real estate brokerage looking to hire more real estate agents. We need to list everything we have to offer as a company so real estate agents will join our company. this is our company website: www.Marlowrealty.example .

100% COMMISSION NO MONTHLY FEE
$450 Flat Transaction FEE

What We Offer:
24/7 Office Access
Free E & O Insurance for 1st Year
Free Online CE and PLE
Free 1,000 Business Cards
Free Professional Social Media Marketing
Free Printing, Scanning, and Copies
Free Buyer and Seller Presentation Packages
Free Filquay Cloud Based Document Management Access
Access to our Internal Brokerage Forum
Company Profit Sharing!
Private Offices Available to Rent

*Lead Generation Software with over 3,000 Leads
*10 Leads to Start
* Free Personal CRM and Website
*Restrictions and Rules apply

Company Address:
4817 Amberfield Road
Suite 512
Fairfax, VA 22194
Phone: 703-555-0147
email: info@marlowrealty.example

Target Market(s)

Real Estate Agents

Industry/Entity Type

Real Estate

Colors
0555a3
ffffff

Requirements
Must have
• 100% COMMISSION NO MONTHLY FEE
$450 Flat Transaction FEE

What We Offer:
24/7 Office Access
Free Online CE and PLE
Free 1,000 Business Cards
Company Profit Sharing!

*10 Leads to Start

Company Address:
4817 Amberfield Road
Suite 512
Fairfax, VA 22194
Phone: 703-555-0147

```html
<!DOCTYPE html>
<html lang="en">
<head>
<meta charset="utf-8">
<title>Marlow Realty – Agent Recruiting Flyer</title>
<link rel="stylesheet" href="https://fonts.googleapis.com/css2?family=Poppins:wght@300;400;500;600;700;800&display=swap">
<style>
  :root {
    --navy: #2c3a88;
    --brand-blue: #0555a3;
    --sky: #1e9bd8;
    --ice: #d6eef8;
    --ice-soft: #eef8fc;
    --white: #ffffff;
    --ink: #1f2a5c;
    --stage: #e4e5e7;
  }
  * { box-sizing: border-box; margin: 0; padding: 0; }
  html, body { width: 1200px; height: 1200px; overflow: hidden; }
  body {
    background: var(--stage);
    font-family: "Poppins", Arial, sans-serif;
    color: var(--ink);
    position: relative;
  }
  .flyer {
    position: absolute;
    left: 170px; top: 44px;
    width: 860px; height: 1112px;
    background: linear-gradient(180deg, var(--white) 0%, var(--white) 38%, var(--ice-soft) 55%, var(--ice) 86%);
    overflow: hidden;
    box-shadow: 0 6px 22px rgba(0,0,0,.12);
  }
  .hero-photo {
    position: absolute; left: 0; top: 0; width: 860px; height: 380px;
    background:
      linear-gradient(180deg, rgba(255,255,255,0) 50%, var(--white) 100%),
      radial-gradient(ellipse at 55% 45%, #d9b8a2 0%, #c7a896 16%, rgba(190,205,225,.9) 40%, #e7eef6 75%),
      #e7eef6;
  }
  .hero-shapes { position: absolute; left: 0; top: 0; }
  .brand {
    position: absolute; left: 48px; top: 170px;
    display: flex; align-items: center; gap: 14px;
    color: var(--white); font-weight: 600; font-size: 34px; letter-spacing: .5px;
  }
  .brand-mark { width: 22px; height: 22px; background: var(--white); }
  .website {
    position: absolute; right: 34px; top: 28px;
    font-size: 15px; font-weight: 500; color: var(--navy);
  }
  .headline { position: absolute; left: 48px; top: 362px; }
  .headline-main {
    font-size: 70px; font-weight: 800; color: var(--navy);
    line-height: 1; letter-spacing: 1px;
  }
  .headline-sub {
    font-size: 34px; font-weight: 700; color: var(--sky);
    margin: 6px 0 0 170px; line-height: 1;
  }
  .headline-fee {
    font-size: 40px; font-weight: 300; color: var(--ink);
    margin-top: 6px; line-height: 1.1;
  }
  .intro {
    position: absolute; left: 48px; top: 540px; width: 770px;
    font-size: 15px; line-height: 1.45; font-weight: 400;
  }
  .offer { position: absolute; left: 48px; top: 604px; width: 430px; }
  .offer-title { font-size: 18px; font-weight: 700; margin-bottom: 4px; }
  .offer-list { list-style: none; }
  .offer-list li {
    font-size: 15px; line-height: 1.45; font-weight: 500;
    padding-left: 22px; position: relative;
  }
  .offer-list li::before {
    content: ""; position: absolute; left: 2px; top: 8px;
    width: 7px; height: 7px;
    border-top: 2.5px solid var(--navy); border-right: 2.5px solid var(--navy);
    transform: rotate(45deg);
  }
  .perks { position: absolute; left: 500px; top: 606px; width: 360px; }
  .perk {
    background: var(--navy);
    color: var(--white);
    font-weight: 700; font-size: 16px; line-height: 1.3;
    text-transform: uppercase;
    height: 80px; margin-bottom: 12px;
    display: flex; align-items: center;
    padding: 0 30px 0 46px;
    clip-path: polygon(0 0, 100% 0, 100% 100%, 0 100%, 22px 50%);
  }
  .perk-note {
    font-size: 11px; font-style: italic; color: var(--ink);
    text-align: right; padding-right: 30px;
  }
  .contact-band {
    position: absolute; left: 0; bottom: 0; width: 860px; height: 140px;
    background: var(--navy);
    color: var(--white);
    display: flex; flex-direction: column; align-items: center; justify-content: center;
    gap: 6px; font-size: 17px; font-weight: 400;
  }
  .contact-band::before {
    content: ""; position: absolute; left: 0; top: -10px; width: 860px; height: 4px;
    background: var(--sky);
  }
  .contact-row { display: flex; gap: 26px; align-items: center; }
  .contact-item { display: flex; align-items: center; gap: 8px; }
  .contact-icon { width: 20px; height: 20px; }
</style>
</head>
<body>
  <main class="flyer">
    <div class="hero-photo" role="img" aria-label="Photo of two professionals shaking hands"></div>

    <svg class="hero-shapes" width="860" height="380" viewBox="0 0 860 380" aria-hidden="true">
      <polygon points="0,0 340,0 500,240 0,350" fill="var(--navy)"/>
      <polygon points="0,350 500,240 520,252 0,372" fill="var(--white)"/>
      <polygon points="560,0 860,0 860,150" fill="var(--white)"/>
    </svg>

    <div class="brand"><span class="brand-mark"></span>Marlow Realty</div>
    <div class="website">www.Marlowrealty.example</div>

    <header class="headline">
      <h1 class="headline-main">100% COMMISSION</h1>
      <p class="headline-sub">NO MONTHLY FEE</p>
      <p class="headline-fee">$450 Flat Transaction FEE</p>
    </header>

    <p class="intro">We are a real estate brokerage looking to hire more real estate agents. We need to list everything we have to offer as a company so real estate agents will join our company.</p>

    <section class="offer">
      <h2 class="offer-title">What We Offer:</h2>
      <ul class="offer-list">
        <li>24/7 Office Access</li>
        <li>Free E &amp; O Insurance for 1st Year</li>
        <li>Free Online CE and PLE</li>
        <li>Free 1,000 Business Cards</li>
        <li>Free Professional Social Media Marketing</li>
        <li>Free Printing, Scanning, and Copies</li>
        <li>Free Buyer and Seller Presentation Packages</li>
        <li>Free Filquay Cloud Based Document Management Access</li>
        <li>Access to our Internal Brokerage Forum</li>
        <li>Company Profit Sharing!</li>
        <li>Private Offices Available to Rent</li>
      </ul>
    </section>

    <aside class="perks">
      <div class="perk">Lead generation software with over 3,000 leads*</div>
      <div class="perk">10 leads to start*</div>
      <div class="perk">Free personal CRM and website*</div>
      <p class="perk-note">*Restrictions and Rules apply</p>
    </aside>

    <footer class="contact-band">
      <p>4817 Amberfield Road, Suite 512, Fairfax, VA 22194</p>
      <div class="contact-row">
        <span class="contact-item">
          <svg class="contact-icon" viewBox="0 0 20 20" aria-hidden="true">
            <circle cx="10" cy="10" r="10" fill="var(--white)"/>
            <path d="M6.5 5.5c.6-.5 1.3-.4 1.6.2l.8 1.6c.2.5 0 1-.4 1.3l-.6.4c.5 1.2 1.4 2.1 2.6 2.7l.5-.6c.3-.4.9-.5 1.3-.3l1.6.8c.6.3.7 1 .2 1.6l-.8.8c-.6.6-1.6.7-2.4.3-2.3-1.1-4-2.9-5.1-5.2-.4-.8-.2-1.8.4-2.4z" fill="var(--navy)"/>
          </svg>703-555-0147
        </span>
        <span class="contact-item">
          <svg class="contact-icon" viewBox="0 0 20 20" aria-hidden="true">
            <circle cx="10" cy="10" r="10" fill="var(--white)"/>
            <rect x="5" y="6.5" width="10" height="7" rx="1" fill="var(--navy)"/>
            <path d="M5.3 7l4.7 3.6L14.7 7" stroke="var(--white)" stroke-width="1" fill="none"/>
          </svg>info@marlowrealty.example
        </span>
      </div>
      <p>Licensed in: D.C, Maryland &amp; Virginia</p>
    </footer>
  </main>
</body>
</html>
```